NEW Business Cards!
CNC Machine Shop Business Cards
Simple
Dale Workman
248 North Route 371
Kelvale, Texas 75418
WorkmanIronCraft@mailbox-example.com
www.WorkmanIronCraft.example
We also need this person on the same card somehow:
Travis Workman
Cell - 555.218.7730
Fax - Same
email - Same
In-House Services:
CNC Milling
CNC Turning
CNC Bending
Water Jet Cutting
Powder Coating

```html
<!DOCTYPE html>
<html lang="en">
<head>
<meta charset="utf-8">
<title>Workman Metal Works – Business Card</title>
<link rel="stylesheet" href="https://fonts.googleapis.com/css2?family=Open+Sans:wght@400;600;700&display=swap">
<style>
  :root {
    --bg: #eeeeee;
    --card: #ffffff;
    --blue-light: #3fb3ee;
    --blue-mid: #1a8fdc;
    --blue-dark: #0b5fb0;
    --gold-light: #d9c08a;
    --gold-dark: #7b6128;
    --brand-blue: #1a5f9e;
    --grey-text: #555555;
    --white: #ffffff;
  }
  * { margin: 0; padding: 0; box-sizing: border-box; }
  html, body { width: 1200px; height: 982px; overflow: hidden; }
  body {
    background: var(--bg);
    font-family: "Open Sans", Arial, sans-serif;
    position: relative;
  }
  .card {
    position: absolute;
    top: 112px;
    width: 438px;
    height: 764px;
    background: var(--card);
    box-shadow: 0 3px 10px rgba(0,0,0,0.25);
    overflow: hidden;
  }
  .card--front { left: 106px; }
  .card--back { left: 650px; }

  .brand {
    position: absolute;
    display: flex;
    align-items: center;
    gap: 14px;
  }
  .brand__square {
    width: 44px; height: 44px;
    background: var(--brand-blue);
  }
  .brand__name {
    color: var(--brand-blue);
    font-weight: 700;
    font-size: 30px;
    line-height: 1;
    white-space: nowrap;
  }
  .card--front .brand { left: 36px; top: 230px; }
  .card--front .brand__name { font-size: 27px; }
  .card--back .brand {
    left: 0; right: 0; top: 235px;
    justify-content: center;
  }

  .band { position: absolute; left: 0; top: 330px; width: 438px; height: 434px; }

  .contact {
    position: absolute;
    left: 0; right: 0; top: 422px;
    text-align: center;
    color: var(--white);
  }
  .contact__name { font-size: 26px; font-weight: 700; line-height: 32px; margin-bottom: 10px; }
  .contact__lines { list-style: none; font-size: 16px; font-weight: 700; line-height: 22px; }
  .contact__second { margin-top: 14px; }
  .contact__second .contact__name { font-size: 22px; line-height: 28px; margin-bottom: 4px; }

  .services {
    position: absolute;
    left: 0; right: 0; top: 497px;
    text-align: center;
    color: var(--grey-text);
  }
  .services__title { font-size: 30px; font-weight: 400; margin-bottom: 26px; }
  .services__list { list-style: none; font-size: 19px; line-height: 26px; }
  .services__list li::before { content: "• "; }
</style>
</head>
<body>
  <section class="card card--front">
    <div class="brand">
      <span class="brand__square"></span>
      <span class="brand__name">Workman Metal Works</span>
    </div>
    <svg class="band" viewBox="0 0 438 434" aria-hidden="true">
      <defs>
        <linearGradient id="gold" x1="0" x2="1">
          <stop offset="0" stop-color="#7b6128"/>
          <stop offset="0.5" stop-color="#d9c08a"/>
          <stop offset="1" stop-color="#7b6128"/>
        </linearGradient>
        <linearGradient id="blue" x1="0" y1="0" x2="0" y2="1">
          <stop offset="0" stop-color="#3fb3ee"/>
          <stop offset="0.45" stop-color="#1a8fdc"/>
          <stop offset="1" stop-color="#0b5fb0"/>
        </linearGradient>
      </defs>
      <path d="M0 36 Q219 -20 438 24 L438 434 L0 434 Z" fill="url(#gold)"/>
      <path d="M0 56 Q219 6 438 46 L438 434 L0 434 Z" fill="#ffffff"/>
      <path d="M0 66 Q219 20 438 58 L438 434 L0 434 Z" fill="url(#blue)"/>
    </svg>
    <div class="contact">
      <p class="contact__name">Dale Workman</p>
      <ul class="contact__lines">
        <li>248 North Route 371</li>
        <li>Kelvale, Texas 75418</li>
        <li>Cell: 555.304.1186</li>
        <li>Fax: 555.930.4472</li>
        <li>WorkmanIronCraft@mailbox-example.com</li>
        <li>www.WorkmanIronCraft.example</li>
      </ul>
      <div class="contact__second">
        <p class="contact__name">Travis Workman</p>
        <ul class="contact__lines">
          <li>Cell: 555.218.7730</li>
        </ul>
      </div>
    </div>
  </section>

  <section class="card card--back">
    <div class="brand">
      <span class="brand__square"></span>
      <span class="brand__name">Workman</span>
    </div>
    <div class="services">
      <h2 class="services__title">In-House Services:</h2>
      <ul class="services__list">
        <li>CNC Milling</li>
        <li>CNC Turning</li>
        <li>CNC Bending</li>
        <li>Water Jet Cutting</li>
        <li>Powder Coating</li>
      </ul>
    </div>
  </section>
</body>
</html>
```